New website for Pollard Law Firm at www.keepwinning-example.com

We are a professional law firm located in the Nashville, Tennessee USA area. We focus on personal injury law. We are looking for a slick new website that is user friendly for updating with new blogs, videos, etc. The primary colors should be red, black, and white. It should load extremely fast and have a good mobile component. The pages for the design will include a home page, about us, news, contact us, and practice page. The practice page will be copied for all the practice areas including motor vehicle accidents, slip and fall accidents, dog bites, etc. We have included an image which we would like to include in the new site which shows the color scheme The image is called banner-Car Wreck. The new website should NOT have gavels, court houses, law books, scales or the typical images for a law firm.

Target Market(s)

People in Tennessee involved in accidents

Industry/Entity Type

Legal services, law firm

Coding

Coded - Design and coding required

Number of Pages Required

5+ page

Font styles to use
Serif

Colors
EB3D1F
EC4F4E
F09395
F8D3D4
FCEDEE

Requirements
Should not have
• Gavels, columns, scales, law related images

```html
<!DOCTYPE html>
<html lang="en">
<head>
<meta charset="utf-8">
<title>News – Keep Winning</title>
<link href="https://fonts.googleapis.com/css2?family=Open+Sans:wght@400;600;700&display=swap" rel="stylesheet">
<style>
:root{
  --red:#e50505;
  --ink:#111111;
  --text:#2b2b2b;
  --muted:#8a8a8a;
  --line:#e3e3e3;
  --footer:#121212;
  --white:#ffffff;
}
*{margin:0;padding:0;box-sizing:border-box}
html,body{width:965px;height:1200px;overflow:hidden;background:var(--white)}
body{position:relative;font-family:'Open Sans',sans-serif;color:var(--text)}
.abs{position:absolute}
a{color:inherit;text-decoration:none}

/* header */
.site-header{left:0;top:0;width:965px;height:64px;background:var(--white)}
.brand{left:70px;top:14px;font-size:26px;font-weight:700;color:var(--red);letter-spacing:.2px}
.nav a{position:absolute;top:24px;font-size:11.5px;color:var(--ink)}
.nav a.active{color:var(--red);font-weight:600;text-decoration:underline}
.phone-badge{left:672px;top:21px;width:22px;height:22px;border-radius:50%;background:#eeeeee}
.phone-num{left:700px;top:24px;font-size:11.5px;color:var(--ink);font-weight:600}
.btn-contact{left:814px;top:19px;width:80px;height:27px;background:var(--red);color:var(--white);font-size:10.5px;font-weight:700;display:flex;align-items:center;justify-content:center;border-radius:2px}

/* banner */
.page-banner{left:0;top:64px;width:965px;height:121px;background:linear-gradient(90deg,#3e3a36 0%,#57504a 45%,#6a2a22 58%,#4a4440 75%,#3a3633 100%)}
.banner-rule{left:0;top:185px;width:965px;height:3px;background:var(--red)}
.page-title{left:0;top:106px;width:965px;text-align:center;font-size:28px;font-weight:700;color:var(--white)}

/* article */
.post-title{left:71px;top:247px;font-size:19.5px;font-weight:600;color:var(--red)}
.post-photo{left:71px;top:287px;width:581px;height:239px;background:linear-gradient(120deg,#3a3f45 0%,#8a8d90 40%,#c9cbcd 65%,#9b9ea1 100%)}
.post-meta{left:71px;top:539px;font-size:9px;color:var(--ink);display:flex;align-items:center;gap:4px}
.post-meta .label{color:var(--muted)}
.post-body{left:71px;top:580px;width:575px;font-size:10.6px;line-height:16.7px;color:var(--text);hyphens:auto}
.post-body p{margin-bottom:13px}
.divider{left:71px;top:790px;width:572px;height:1px;background:var(--line)}
.share-label{left:71px;top:813px;width:572px;text-align:center;font-size:10.5px;color:#666}
.pill{top:848px;width:103px;height:29px;border-radius:15px;display:flex;align-items:center;justify-content:center;font-size:9px;font-weight:600;letter-spacing:.3px}
.pill.prev{left:71px;border:1px solid #c8c8c8;color:#9a9a9a}
.pill.next{left:540px;border:1px solid var(--red);color:var(--red)}
.share-dot{top:848px;width:29px;height:29px;border-radius:50%}

/* sidebar */
.contact-card{left:677px;top:253px;width:217px;height:241px;background:var(--white);box-shadow:0 0 10px rgba(0,0,0,.08)}
.card-title{left:697px;top:266px;font-size:19.5px;font-weight:600;color:var(--red)}
.card-text{left:697px;top:302px;width:183px;font-size:10.3px;line-height:14.1px;color:var(--ink);hyphens:auto}
.btn-book{left:697px;top:445px;width:146px;height:30px;border:1px solid var(--ink);display:flex;align-items:center;justify-content:center;font-size:10.5px;font-weight:600;color:var(--ink);border-radius:2px}

/* footer */
.site-footer{left:0;top:941px;width:965px;height:225px;background:var(--footer)}
.foot-head{top:991px;font-size:15.5px;font-weight:600;color:var(--red)}
.foot-list{top:1022px;list-style:none;font-size:10.5px;color:var(--white)}
.foot-list li{height:21.2px}
.foot-list li.active{color:var(--red);text-decoration:underline}
.contact-row{left:416px;font-size:10.5px;color:var(--white);display:flex;gap:8px;line-height:16px}
.map-box{left:645px;top:996px;width:249px;height:129px;background:linear-gradient(135deg,#f1f1ef,#e4e6e4);border-radius:2px}
.bottom-bar{left:0;top:1166px;width:965px;height:34px;background:var(--red)}
.copyright{left:70px;top:1174px;font-size:10.5px;color:var(--white)}
.social-mini{top:1177px;width:10px;height:10px;border-radius:50%;background:var(--white)}
</style>
</head>
<body>

<header class="abs site-header">
  <div class="abs brand">Keep Winning</div>
  <nav class="nav">
    <a style="left:367px">Home</a>
    <a style="left:427px">About Us</a>
    <a style="left:504px">Practice Areas</a>
    <a class="active" style="left:607px">News</a>
  </nav>
  <div class="abs phone-badge">
    <svg width="22" height="22" viewBox="0 0 22 22"><path d="M8 6.5l1.6-.4 1 2.3-1 .8a6 6 0 0 0 3 3l.8-1 2.3 1-.4 1.6c-3.8.5-7.8-3.5-7.3-7.3z" fill="#e50505"/></svg>
  </div>
  <div class="abs phone-num">(555) 014-2280</div>
  <a class="abs btn-contact">Contact Us</a>
</header>

<section class="abs page-banner" role="img" aria-label="Roadside scene with a red warning triangle in front of a damaged car"></section>
<div class="abs banner-rule"></div>
<h1 class="abs page-title">News</h1>

<h2 class="abs post-title">Insurance Company Pays for Facial Fractures</h2>
<div class="abs post-photo" role="img" aria-label="Hands filling in an insurance claim form on a clipboard beside a car"></div>

<div class="abs post-meta">
  <svg width="12" height="12" viewBox="0 0 12 12"><rect x="1" y="2" width="10" height="9" fill="none" stroke="#e50505" stroke-width="1.3"/><rect x="1" y="2" width="10" height="2.5" fill="#e50505"/><path d="M3.5 0.5v2.5M8.5 0.5v2.5" stroke="#e50505" stroke-width="1.3"/></svg>
  <span>20 May 2020</span>
  <svg style="margin-left:12px" width="11" height="12" viewBox="0 0 11 12"><circle cx="5.5" cy="3.5" r="2.6" fill="none" stroke="#e50505" stroke-width="1.2"/><path d="M1 11.5c0-3 2-4.5 4.5-4.5s4.5 1.5 4.5 4.5z" fill="none" stroke="#e50505" stroke-width="1.2"/></svg>
  <span class="label">Posted by:</span><span>Daniel Marsh</span>
</div>

<article class="abs post-body">
  <p>Lorem Ipsum is simply dummy text of the printing and typesetting industry. Lorem Ipsum has been the industry's standard dummy text ever since the 1500s, when an unknown printer took a galley of type and scrambled it to make a type specimen book.</p>
  <p>It has survived not only five centuries, but also the leap into electronic typesetting, remaining essentially unchanged. It was popularised in the 1960s with the release of Typeleaf sheets containing Lorem Ipsum passages, and more recently with desktop publishing software like Pressline Layout including versions of Lorem Ipsum.</p>
  <p>Lorem Ipsum is simply dummy text of the printing and typesetting industry. Lorem Ipsum has been the industry's standard dummy text ever since the 1500s, when an unknown printer took a galley of type and scrambled it to make a type specimen book.</p>
</article>

<div class="abs divider"></div>
<div class="abs share-label">Share Blog:</div>
<a class="abs pill prev">«&nbsp; PREV POST</a>
<div class="abs share-dot" style="left:266px;background:#1da1f2" aria-label="Share"></div>
<div class="abs share-dot" style="left:301px;background:#3b5998" aria-label="Share"></div>
<div class="abs share-dot" style="left:336px;background:#cb2027" aria-label="Share"></div>
<div class="abs share-dot" style="left:372px;background:#c13584" aria-label="Share"></div>
<div class="abs share-dot" style="left:407px;background:#0e76a8" aria-label="Share"></div>
<a class="abs pill next">NEXT POST &nbsp;»</a>

<aside>
  <div class="abs contact-card"></div>
  <h3 class="abs card-title">Get in touch</h3>
  <p class="abs card-text">We at Pollard Law Firm know that finding the right attorney to repre&shy;sent you is a choice not to be taken lightly. That’s why we offer free con&shy;sultations to personal injury clients or a 1 hour paid consultation to all other clients to help you determine the needs of your case and whether we are good fit.</p>
  <a class="abs btn-book">Book an Appointment</a>
</aside>

<footer>
  <div class="abs site-footer"></div>
  <h4 class="abs foot-head" style="left:70px">Quick Link</h4>
  <ul class="abs foot-list" style="left:71px">
    <li>Home</li><li>About Us</li><li>Practice Areas</li><li class="active">News</li><li>Contact Us</li>
  </ul>
  <h4 class="abs foot-head" style="left:224px">Practice Areas</h4>
  <ul class="abs foot-list" style="left:224px">
    <li>Motor Vehicle Accidents</li><li>Slip and Fall Accidents</li><li>Dog Bites</li><li>Business Law</li><li>View All Practice</li>
  </ul>
  <h4 class="abs foot-head" style="left:416px">Conatct info</h4>
  <div class="abs contact-row" style="top:1023px">
    <svg width="12" height="15" viewBox="0 0 12 15"><path d="M6 0a5.5 5.5 0 0 0-5.5 5.5C.5 9.5 6 15 6 15s5.5-5.5 5.5-9.5A5.5 5.5 0 0 0 6 0z" fill="#e50505"/><circle cx="6" cy="5.5" r="2" fill="#121212"/></svg>
    <span>118 Harbor Lane<br>Millbrook, TN&nbsp;&nbsp; 37000</span>
  </div>
  <div class="abs contact-row" style="top:1072px">
    <svg width="12" height="12" viewBox="0 0 12 12"><path d="M1 1.5L3.5 1l1.4 3-1.3 1a7 7 0 0 0 3.4 3.4l1-1.3 3 1.4-.5 2.5C5.6 11.5.5 6.4 1 1.5z" fill="#e50505"/></svg>
    <span>(555) 014-2280</span>
  </div>
  <div class="abs contact-row" style="top:1107px">
    <svg width="13" height="10" viewBox="0 0 13 10" style="margin-top:3px"><rect width="13" height="10" fill="#e50505"/><path d="M0 0l6.5 5.5L13 0" fill="none" stroke="#121212" stroke-width="1.2"/></svg>
    <span>info@keepwinning-example.com</span>
  </div>
  <div class="abs map-box" role="img" aria-label="Street map showing the office location"></div>

  <div class="abs bottom-bar"></div>
  <div class="abs copyright">Copyright © 2021 Keep Winning. All Rights Reserved</div>
  <div class="abs social-mini" style="left:808px" aria-label="Social link"></div>
  <div class="abs social-mini" style="left:831px" aria-label="Social link"></div>
  <div class="abs social-mini" style="left:857px" aria-label="Social link"></div>
  <div class="abs social-mini" style="left:883px" aria-label="Social link"></div>
</footer>

</body>
</html>
```